Investment company needing business card

We are wanting a business card which looks sharp and easy on the eye. We are thinking of having a business card with the logo embossed on it, to really make it stand out. We will only have a small amount of information of the business card, person's name, position, email address and phone number

Contact Information for Business Card

Danica Pruett
Executive Assistant
+64 21 547 3162
danicap@harwellcapital.co.nz

Requirements
Must have
• Embossed logo
Should not have
• Not to be busy

```html
<!DOCTYPE html>
<html lang="en">
<head>
<meta charset="utf-8">
<title>Harwell Capital – Business Card</title>
<link href="https://fonts.googleapis.com/css2?family=Open+Sans:wght@400;600;700&display=swap" rel="stylesheet">
<style>
  :root {
    --green: #1faa68;
    --grey: #5b5c5e;
    --text: #3c3d3f;
    --card: #ffffff;
    --backdrop: #d9dadb;
  }
  * { margin: 0; padding: 0; box-sizing: border-box; }
  html, body { width: 1200px; height: 900px; overflow: hidden; }
  body {
    background: var(--backdrop);
    font-family: "Open Sans", Arial, sans-serif;
    position: relative;
  }
  .card {
    position: absolute;
    width: 665px;
    height: 380px;
    background: var(--card);
    border-radius: 22px;
    box-shadow: 0 6px 18px rgba(0,0,0,0.18);
    overflow: hidden;
  }
  .card--front { left: 60px; top: 50px; }
  .card--back { left: 475px; top: 470px; }

  .brand {
    position: absolute;
    display: flex;
    align-items: center;
    gap: 14px;
  }
  .brand__square {
    width: 40px; height: 40px;
    background: var(--green);
  }
  .brand__name {
    color: var(--green);
    font-weight: 700;
    font-size: 30px;
    letter-spacing: 1px;
    text-transform: uppercase;
    line-height: 1;
  }
  .card--front .brand { left: 44px; top: 70px; }
  .card--back .brand { left: 50%; top: 50%; transform: translate(-50%, -50%); }
  .card--back .brand__square { width: 48px; height: 48px; }
  .card--back .brand__name { font-size: 36px; }

  .person {
    position: absolute;
    left: 0; top: 258px;
    display: flex;
    align-items: stretch;
  }
  .person__bar { width: 30px; height: 46px; background: var(--green); }
  .person__rule { width: 3px; height: 46px; background: var(--grey); margin-left: 8px; }
  .person__text { margin-left: 10px; display: flex; flex-direction: column; justify-content: center; }
  .person__name { color: var(--green); font-weight: 700; font-size: 19px; line-height: 1.15; text-transform: uppercase; }
  .person__role { color: var(--text); font-size: 16px; line-height: 1.2; }

  .contact {
    position: absolute;
    right: 28px; top: 120px;
    list-style: none;
    display: flex;
    flex-direction: column;
    gap: 8px;
  }
  .contact__item {
    display: flex;
    align-items: center;
    justify-content: flex-end;
    gap: 10px;
    color: var(--text);
    font-size: 17px;
  }
  .contact__icon { width: 20px; height: 20px; flex: none; }
</style>
</head>
<body>

  <section class="card card--front" aria-label="Business card front">
    <div class="brand">
      <span class="brand__square"></span>
      <span class="brand__name">Harwell Capital</span>
    </div>

    <ul class="contact">
      <li class="contact__item">
        <span>+64 21 547 3162</span>
        <svg class="contact__icon" viewBox="0 0 20 20" aria-hidden="true">
          <circle cx="10" cy="10" r="10" fill="var(--green)"/>
          <path d="M7 5.5 L8.6 5.5 L9.3 8 L8.3 9 Q9.3 11 11 11.8 L12 10.8 L14.5 11.5 L14.5 13 Q14.5 14.3 13 14.2 Q6 13.5 5.8 7 Q5.8 5.5 7 5.5 Z" fill="#fff"/>
        </svg>
      </li>
      <li class="contact__item">
        <span>danicap@harwellcapital.co.nz</span>
        <svg class="contact__icon" viewBox="0 0 20 20" aria-hidden="true">
          <circle cx="10" cy="10" r="10" fill="var(--green)"/>
          <rect x="5" y="6.5" width="10" height="7" fill="#fff"/>
          <path d="M5 6.5 L10 10.5 L15 6.5" fill="none" stroke="var(--green)" stroke-width="1"/>
        </svg>
      </li>
      <li class="contact__item">
        <span>www.harwellcapital.co.nz</span>
        <svg class="contact__icon" viewBox="0 0 20 20" aria-hidden="true">
          <circle cx="10" cy="10" r="10" fill="var(--green)"/>
          <g fill="none" stroke="#fff" stroke-width="1.1">
            <circle cx="10" cy="10" r="5"/>
            <ellipse cx="10" cy="10" rx="2.2" ry="5"/>
            <line x1="5" y1="10" x2="15" y2="10"/>
          </g>
        </svg>
      </li>
    </ul>

    <div class="person">
      <span class="person__bar"></span>
      <span class="person__rule"></span>
      <div class="person__text">
        <span class="person__name">Danica Pruett</span>
        <span class="person__role">Executive Assistant</span>
      </div>
    </div>
  </section>

  <section class="card card--back" aria-label="Business card back">
    <div class="brand">
      <span class="brand__square"></span>
      <span class="brand__name">Harwell Capital</span>
    </div>
  </section>

</body>
</html>
```